Newsletter Design Project

I need a new design for a monthly newsletter that I do for Academy of Lifelong Pursuits Brisbane. I have been doing the same thing since 2009. We are based in Brisbane and we run classes for semi retired and retired people. I write about social activities, class activities, vacancies etc. I take photos and include them we hhave a logo that I always use. and would just like the newsletter to look different and fresh. The logo is Blue

```html
<!DOCTYPE html>
<html lang="en">
<head>
<meta charset="utf-8">
<title>Academy of Lifelong Pursuits Brisbane – Campus Newsletter July 2013</title>
<link href="https://fonts.googleapis.com/css2?family=Caladea:wght@400;700&family=Didact+Gothic&display=swap" rel="stylesheet">
<style>
  :root {
    --page: #fdf2f2;
    --blue-light: #abc3e5;
    --blue-deep: #5a83c5;
    --teal: #30879a;
    --cream: #f3dfb5;
    --rose: #e7b8b8;
    --rose-photo: #d99292;
    --ink: #3f3f3f;
    --rule: #c9c3dd;
  }
  * { margin: 0; padding: 0; box-sizing: border-box; }
  html, body { width: 927px; height: 1200px; overflow: hidden; background: var(--page); }
  body { position: relative; font-family: "Caladea", Cambria, serif; color: var(--ink); }

  .masthead {
    position: absolute; left: 55px; top: 55px; width: 633px; height: 225px;
    background: linear-gradient(180deg, var(--blue-light), var(--blue-deep));
    border: 1px solid #7b9ccf;
    box-shadow: 2px 3px 4px rgba(0,0,0,.25);
  }
  .brand {
    position: absolute; left: 39px; top: 9px; width: 568px; height: 204px;
    background: #fff5f5; border: 2px solid #111;
    display: flex; align-items: center; justify-content: center;
  }
  .brand-name { font-weight: 400; font-size: 52px; line-height: 1; color: var(--ink); }

  .issue-tab {
    position: absolute; left: 703px; top: 56px; width: 169px; height: 223px;
    background: var(--teal); box-shadow: 2px 3px 4px rgba(0,0,0,.25);
    font-family: "Didact Gothic", "Century Gothic", sans-serif; font-size: 26px;
    color: var(--cream); text-align: right; padding: 30px 12px 0 0; line-height: 62px;
  }

  .title-bar {
    position: absolute; left: 56px; top: 295px; width: 816px; height: 69px;
    background: var(--rose); border: 1px solid #7f9bd0;
    box-shadow: 1px 2px 3px rgba(0,0,0,.2);
    display: flex; align-items: center; justify-content: center;
    font-size: 34px; font-weight: 400; color: #4a4444;
  }

  .column { position: absolute; top: 380px; font-size: 20.5px; line-height: 37px; }
  .column p { margin-bottom: 16px; }
  .column-left { left: 66px; width: 388px; }
  .column-left h2 { text-align: center; font-size: 22px; font-weight: 700; margin: 3px 0 15px; line-height: 37px; }
  .column-left p { text-indent: 54px; }
  .column-right { left: 493px; width: 355px; }
  .column-right strong { font-weight: 700; }
  .column-divider { position: absolute; left: 464px; top: 452px; width: 1px; height: 409px; background: var(--rule); }

  .photo-band {
    position: absolute; left: 65px; top: 969px; width: 797px; height: 167px;
    background: linear-gradient(180deg, var(--blue-light), var(--blue-deep));
    border: 1px solid #7b9ccf; box-shadow: 2px 3px 4px rgba(0,0,0,.25);
  }
  .photo-slot {
    position: absolute; top: 21px; width: 212px; height: 130px;
    background: var(--rose-photo); border: 1px solid #8fa3cc;
    box-shadow: 1px 2px 3px rgba(0,0,0,.25);
    display: flex; align-items: center; justify-content: center;
    font-size: 20px; color: #4a3c3c;
  }
  .photo-slot-1 { left: 53px; }
  .photo-slot-2 { left: 310px; }
  .photo-slot-3 { left: 550px; }
</style>
</head>
<body>
  <header class="masthead">
    <div class="brand">
      <span class="brand-name">Lifelong Pursuits</span>
    </div>
  </header>
  <div class="issue-tab">Campus<br>Newsletter<br>July 2013</div>

  <h1 class="title-bar">Academy of Lifelong Pursuits, Brisbane</h1>

  <section class="column column-left">
    <h2>Winter School 2013</h2>
    <p>Friday, July 5<sup style="font-size:12px">th</sup>, saw the last classes mark the end of a very successful Winter School. There were more than fifty diverse classes covering everything from The History of Barnaby Quill to Understanding your PocketPhone and SlateTab.</p>
    <p>Marion Welsh explained how to keep our bones healthy and keynote speaker, Clive Denholm, shared his amusing autobiography.</p>
    <p>The sessions were well supported and everyone was pleased with the range of courses available.</p>
  </section>

  <div class="column-divider"></div>

  <section class="column column-right">
    <p><strong>A big thank you goes out to the Winter School Committee:</strong>&nbsp; Ruth Carmody, Joan Pedersen, Joan Whitfield, Neil Parsons, Ron Mabey, Barry Cole and Barry Keogh.</p>
    <p><strong>Also thanks to the tech team:</strong> Barry Cole, Edith Marr, Spud Hennessy, and Alan Rossiter.</p>
    <p><strong>And of course:</strong> Barry Cole for his very professional new online bookings system, the office staff who went above and beyond during their “holiday break”, and all the selfless volunteers and entertaining speakers</p>
  </section>

  <section class="photo-band">
    <div class="photo-slot photo-slot-1" role="img" aria-label="Photo from Winter School"></div>
    <div class="photo-slot photo-slot-2" role="img" aria-label="Photo from Winter School">Insert photos here</div>
    <div class="photo-slot photo-slot-3" role="img" aria-label="Photo from Winter School"></div>
  </section>
</body>
</html>
```